Business cards and stationary
Venoki Imaging, llc
Professional
Miriam Colfax. Dana Pruitt
Owners
17 Harrow Lane
Bloomingburg, ny 12721 (Miriam )
52 Willowby Road
New Windsor, NY 12553 ( Dana )
Miriam 914-555-0142. /. Dana 845-555-0197
Juniper41@mailvex.com

```html
<!DOCTYPE html>
<html lang="en">
<head>
<meta charset="utf-8">
<title>Venoki Imaging, llc – Business Card</title>
<link href="https://fonts.googleapis.com/css2?family=Cinzel:wght@400;600&display=swap" rel="stylesheet">
<style>
  :root {
    --bg: #e9e9ec;
    --card: #ffffff;
    --purple: #9c1b8c;
    --purple-dark: #7d1471;
    --blue: #2b7cc0;
    --ink: #1f5f9a;
    --white: #ffffff;
  }
  * { margin: 0; padding: 0; box-sizing: border-box; }
  html, body { width: 1200px; height: 838px; overflow: hidden; }
  body {
    background: var(--bg);
    font-family: "Cinzel", serif;
    position: relative;
  }
  .card {
    position: absolute;
    top: 265px;
    width: 540px;
    height: 309px;
    background: var(--card);
    box-shadow: 0 6px 18px rgba(0,0,0,0.18);
    overflow: hidden;
  }
  .card-back { left: 40px; display: flex; }
  .card-front { left: 620px; display: flex; flex-direction: column; align-items: center; justify-content: center; }

  .brand-mark { display: flex; align-items: center; gap: 8px; color: var(--blue); font-weight: 600; }
  .brand-mark .dot { width: 14px; height: 14px; border-radius: 50%; background: var(--purple); }

  .card-front .brand-mark { font-size: 46px; }
  .card-front .brand-mark .dot { width: 26px; height: 26px; }
  .card-front .web { margin-top: 22px; font-size: 13px; letter-spacing: 1.5px; color: var(--ink); }

  .identity-panel {
    width: 190px;
    height: 100%;
    padding: 0 16px;
    display: flex;
    flex-direction: column;
    align-items: center;
    justify-content: center;
    text-align: center;
    border-right: 6px solid var(--blue);
    position: relative;
  }
  .identity-panel .brand-mark { font-size: 24px; }
  .company-name { margin-top: 14px; font-size: 15px; font-weight: 600; color: var(--ink); letter-spacing: 0.5px; }
  .tagline { margin-top: 4px; font-size: 7.5px; color: var(--purple); letter-spacing: 1px; }

  .contact-panel {
    flex: 1;
    background: linear-gradient(135deg, var(--purple) 0%, var(--purple-dark) 100%);
    color: var(--white);
    padding: 34px 28px 30px;
    display: flex;
    flex-direction: column;
    justify-content: space-between;
  }
  .owners { font-size: 15px; letter-spacing: 1px; }
  .contacts { list-style: none; font-size: 11px; letter-spacing: 0.8px; }
  .contacts li { display: flex; align-items: center; gap: 8px; margin-top: 6px; }
  .contacts svg { width: 14px; height: 14px; flex: none; }
</style>
</head>
<body>
  <section class="card card-back" aria-label="Business card back">
    <div class="identity-panel">
      <div class="brand-mark"><span class="dot"></span>Venoki</div>
      <p class="company-name">Venoki Imaging, llc</p>
      <p class="tagline">Mobile Diagnostic Imaging</p>
    </div>
    <div class="contact-panel">
      <p class="owners">Miriam Colfax &nbsp;Dana Pruitt</p>
      <ul class="contacts">
        <li>
          <svg viewBox="0 0 14 14"><circle cx="7" cy="7" r="7" fill="#fff"/><path d="M4.5 3.8l1.3-.3.7 1.8-.9.6a5 5 0 0 0 2.5 2.5l.6-.9 1.8.7-.3 1.3C7 9.8 4.2 7 4.5 3.8z" fill="var(--purple)"/></svg>
          914-555-0142
        </li>
        <li>
          <svg viewBox="0 0 14 14"><circle cx="7" cy="7" r="7" fill="#fff"/><path d="M4.5 3.8l1.3-.3.7 1.8-.9.6a5 5 0 0 0 2.5 2.5l.6-.9 1.8.7-.3 1.3C7 9.8 4.2 7 4.5 3.8z" fill="var(--purple)"/></svg>
          845-555-0197
        </li>
        <li>
          <svg viewBox="0 0 14 14"><circle cx="7" cy="7" r="7" fill="#fff"/><circle cx="7" cy="7" r="4" fill="none" stroke="var(--purple)" stroke-width="1"/><path d="M3 7h8M7 3c-2 2.5-2 5.5 0 8M7 3c2 2.5 2 5.5 0 8" fill="none" stroke="var(--purple)" stroke-width="0.8"/></svg>
          www.venokidomain.com
        </li>
      </ul>
    </div>
  </section>

  <section class="card card-front" aria-label="Business card front">
    <div class="brand-mark"><span class="dot"></span>Venoki</div>
    <p class="web">www.venokidomain.com</p>
  </section>
</body>
</html>
```